Digital Menu Board for Restaurant

I want a digital menu board for our new restaurant. I have provided the sample of what I kind of want.
This is to be on a 55 inch tv so it needs to be the correct aspect ratio of 4:5

Font styles to use
Serif
Sans Serif

Colors
f59296
f04a50
ec1f27
ffffff
fffef7
fbed22
ffc214
0592cd
e5519f

Requirements
Must have
• fun, maybe something moving? bright colors on a darker background so it's easy to read or dark font on a light background.

```html
<!DOCTYPE html>
<html lang="en">
<head>
<meta charset="utf-8">
<title>Sandy Coves – Menu Board</title>
<link rel="stylesheet" href="https://fonts.googleapis.com/css2?family=Lobster&family=Yanone+Kaffeesatz:wght@500&family=Cabin:wght@600&family=Andika&family=Fredoka:wght@700&display=swap">
<style>
  :root {
    --bg-dark: #1c0f1c;
    --bg-mid: #2b1628;
    --bg-light: #3a2034;
    --yellow: #f2ef4c;
    --heading-yellow: #f0f05a;
    --white: #ffffff;
    --cream: #fffef7;
    --orange: #ff8a3d;
    --plate: #e9e4dc;
    --tomato: #d8231e;
  }
  * { margin: 0; padding: 0; box-sizing: border-box; }
  html, body { width: 1200px; height: 800px; overflow: hidden; background: var(--bg-dark); }
  .board {
    position: relative;
    width: 1200px;
    height: 800px;
    overflow: hidden;
    background:
      repeating-linear-gradient(180deg, rgba(255,255,255,0.025) 0 2px, transparent 2px 62px),
      radial-gradient(ellipse at 50% 45%, var(--bg-light) 0%, var(--bg-mid) 45%, var(--bg-dark) 100%);
  }
  .brand {
    position: absolute;
    left: 34px;
    top: 54px;
    display: flex;
    align-items: center;
    gap: 12px;
  }
  .brand-dot { width: 30px; height: 30px; border-radius: 50%; background: var(--orange); }
  .brand-name { font-family: 'Lobster', cursive; font-size: 44px; color: var(--orange); line-height: 1; }
  .combo { position: absolute; left: 745px; top: 28px; display: flex; align-items: stretch; }
  .combo-title {
    font-family: 'Fredoka', sans-serif;
    font-weight: 700;
    font-size: 35px;
    line-height: 44px;
    color: var(--white);
    padding-right: 14px;
    border-right: 2px solid var(--white);
    height: 88px;
    margin-top: 4px;
  }
  .combo-list {
    list-style: none;
    padding-left: 18px;
    font-family: 'Andika', sans-serif;
    font-size: 25px;
    line-height: 30px;
    letter-spacing: 2px;
    color: var(--white);
  }
  .section-title {
    position: absolute;
    font-family: 'Lobster', cursive;
    color: var(--heading-yellow);
    border-bottom: 2px dotted var(--heading-yellow);
    line-height: 1.2;
  }
  .section-greens { left: 36px; top: 186px; width: 456px; font-size: 50px; padding-left: 5px; padding-bottom: 8px; letter-spacing: 1px; }
  .section-kids { left: 815px; top: 202px; width: 348px; font-size: 31px; text-align: right; padding-right: 5px; padding-bottom: 12px; letter-spacing: 2px; }
  .salad { position: absolute; left: 42px; width: 460px; }
  .salad-name {
    display: inline-block;
    font-family: 'Cabin', sans-serif;
    font-weight: 600;
    font-size: 35px;
    line-height: 36px;
    color: var(--white);
    border-bottom: 2px solid var(--white);
    margin-bottom: 8px;
    letter-spacing: 1px;
  }
  .salad-desc {
    font-family: 'Yanone Kaffeesatz', sans-serif;
    font-weight: 500;
    font-size: 29px;
    line-height: 28px;
    color: var(--yellow);
    letter-spacing: 0.8px;
  }
  .salad-north { top: 282px; }
  .salad-west { top: 436px; left: 46px; }
  .salad-east { top: 617px; }
  .kids-list {
    position: absolute;
    right: 42px;
    top: 282px;
    list-style: none;
    text-align: right;
    font-family: 'Yanone Kaffeesatz', sans-serif;
    font-weight: 500;
    font-size: 31px;
    line-height: 34px;
    letter-spacing: 1.5px;
    color: var(--cream);
  }
  .salad-photo { position: absolute; left: 830px; top: 500px; width: 370px; height: 300px; }
</style>
</head>
<body>
<main class="board">
  <header class="brand">
    <span class="brand-dot"></span>
    <span class="brand-name">Sandy Coves</span>
  </header>

  <section class="combo">
    <div class="combo-title">COMBO<br>UP!</div>
    <ul class="combo-list">
      <li>Add 1 side and Drink</li>
      <li>Add 1 side and Shake</li>
      <li>Additional Sides</li>
    </ul>
  </section>

  <h2 class="section-title section-greens">Green Shore</h2>

  <article class="salad salad-north">
    <h3 class="salad-name">North Beach Salad:</h3>
    <p class="salad-desc">Pulled Pork and Black beans on a Bed of<br>Romaine, Tomato and Onion with Sweet and<br>Sour Raspberry Pinapple Sauce.</p>
  </article>

  <article class="salad salad-west">
    <h3 class="salad-name">West Side Salad:</h3>
    <p class="salad-desc">BBQ Pulled Pork, Crumbled Bacon, Candied<br>Walnuts, Feta Cheese, Red Onion, Spinach<br>and Lettuce with Ranch Dressing or<br>Raspberry Vinaigrette.</p>
  </article>

  <article class="salad salad-east">
    <h3 class="salad-name">East Side Salad:</h3>
    <p class="salad-desc">Spinach and Lettuce, Chopped Apples,<br>Candied Walnuts, Onion, FetaCheese with<br>Jorvin's Raspberry Vinaigrette<br>Add Chicken:</p>
  </article>

  <h2 class="section-title section-kids">Seashell Finders(kids)</h2>
  <ul class="kids-list">
    <li>Little Cheeseburger</li>
    <li>Pulled Pork sandwich</li>
    <li>Mini Corn Dogs</li>
    <li>Chicken salad sandwich</li>
    <li>Fries/ Onion Rings</li>
  </ul>

  <svg class="salad-photo" viewBox="0 0 370 300" role="img" aria-label="Photo of a plate of fresh Greek salad with tomatoes, cucumber, feta and olives, with a cherry tomato beside it">
    <defs>
      <radialGradient id="salad-fill" cx="0.6" cy="0.6" r="0.6">
        <stop offset="0" stop-color="#5f9a32"/>
        <stop offset="0.7" stop-color="#8bbd4a"/>
        <stop offset="1" stop-color="#b8c98a"/>
      </radialGradient>
    </defs>
    <circle cx="362" cy="300" r="292" fill="var(--plate)"/>
    <circle cx="362" cy="300" r="268" fill="url(#salad-fill)"/>
    <circle cx="42" cy="284" r="25" fill="var(--tomato)"/>
  </svg>
</main>
</body>
</html>
```